Learning Habits- Teaching and Learning Policy

Hi,

The philosophy behind this Teaching and Learning Policy is to equip young people (Age 16-18) for many challenges that lies ahead. The pace of technological advancement is so great that it is probable that many jobs our students will do in their lifetime do not yet even exist. We realise that we need to help develop our students into effective lifelong learners – meaning that they will:

-Need to be independent whilst also being able to work as a team.
-Need to apply many different strategies to help take on new concepts.
-Reflect on current practice, and improve.

I have attached the file which has the basic designs of the 4 different leaner habits and what they entail. Each habit is colour coordinated, so please keep the colours the same.

Collaboration- Blue (royal blue)
Persevering- Red
Planning- Orange
Reflection- Yellow

I would ideally like the poster to be transferable into a powerpoint too.

Thanking you all so much.

Lenka
Updates

Project Deadline Extended Reason: Hi,I am extending this deadline as I will be requesting some changes to the title / slogan.I need the four learning habits have a catchy name which will motivate students.Please send me some suggestions.Thanking you all.Lenka Added Monday, March 28, 2016

Target Market(s)

Teachers and students (age 16-18)

Industry/Entity Type

Education

Font styles to use
Other font styles liked:
• Something friendly to kids- where the a is printed like it is written. Similar to century gothic but more friendly.

Requirements
Must have
• Laid out similar to the the website attached. Interesting, motivational yet educational to students in how they can become lifelong learners.
Nice to have
• I should be able to transfer this to a powerpoint from a poster.
• It can be four posters or one depending on the design.
Should not have
• Each Habit must be colour-coordinated:
• Collaboration- Blue (royal blue)
• Persevering- Red
• Planning- Orange
• Reflection- Yellow
• Thank you,

```html
<!DOCTYPE html>
<html lang="en">
<head>
<meta charset="utf-8">
<title>Learning Habits Poster</title>
<link rel="stylesheet" href="https://fonts.googleapis.com/css2?family=Jost:wght@600&display=swap">
<style>
  :root {
    --backdrop: #ededed;
    --collab-blue: #4f86c8;
    --collab-blue-deep: #3f74b8;
    --persevere-red: #db4a3c;
    --persevere-red-deep: #b42a25;
    --plan-orange: #f7a648;
    --plan-orange-deep: #f29a3e;
    --reflect-yellow: #ece53e;
    --reflect-yellow-soft: #f1ec7a;
    --ink-white: #ffffff;
  }
  html, body {
    margin: 0;
    width: 1200px;
    height: 945px;
    overflow: hidden;
    background: var(--backdrop);
  }
  .canvas {
    position: relative;
    width: 1200px;
    height: 945px;
  }
  .poster {
    position: absolute;
    left: 310px;
    top: 50px;
    width: 595px;
    height: 843px;
    box-shadow: 0 6px 18px rgba(0,0,0,0.18);
  }
  .poster svg { display: block; width: 100%; height: 100%; }
  .habit-label {
    font-family: "Jost", "Century Gothic", sans-serif;
    font-weight: 600;
    fill: var(--ink-white);
    letter-spacing: 1px;
  }
</style>
</head>
<body>
<main class="canvas">
  <section class="poster" aria-label="Learning habits poster">
    <svg viewBox="0 0 595 843" xmlns="http://www.w3.org/2000/svg">
      <defs>
        <linearGradient id="red-sky" x1="0" y1="0" x2="1" y2="1">
          <stop offset="0" stop-color="var(--persevere-red-deep)"/>
          <stop offset=".55" stop-color="var(--persevere-red)"/>
          <stop offset="1" stop-color="#e25a3e"/>
        </linearGradient>
        <linearGradient id="blue-hands" x1="0" y1="0" x2="1" y2="1">
          <stop offset="0" stop-color="var(--collab-blue)"/>
          <stop offset="1" stop-color="var(--collab-blue-deep)"/>
        </linearGradient>
        <linearGradient id="yellow-head" x1="0" y1="0" x2="1" y2="1">
          <stop offset="0" stop-color="var(--reflect-yellow)"/>
          <stop offset="1" stop-color="var(--reflect-yellow-soft)"/>
        </linearGradient>
        <linearGradient id="orange-chart" x1="0" y1="0" x2="1" y2="1">
          <stop offset="0" stop-color="var(--plan-orange-deep)"/>
          <stop offset="1" stop-color="var(--plan-orange)"/>
        </linearGradient>
      </defs>

      <polygon class="segment-collaboration" points="0,0 160,0 295,420 0,490" fill="url(#blue-hands)"
               role="img" aria-label="Photo of joined hands in blue tint"/>
      <polygon class="segment-persevering" points="160,0 595,0 595,212 295,420" fill="url(#red-sky)"
               role="img" aria-label="Photo of a climber on a rock at sunset in red tint"/>
      <polygon class="segment-reflection" points="295,420 595,212 595,843 375,843" fill="url(#yellow-head)"
               role="img" aria-label="Illustration of a head in profile in yellow tint"/>
      <polygon class="segment-planning" points="0,490 295,420 375,843 0,843" fill="url(#orange-chart)"
               role="img" aria-label="Photo of a hand-drawn flowchart in orange tint"/>

      <g class="icon-collaboration">
        <circle cx="164" cy="370" r="62" fill="var(--ink-white)"/>
        <rect x="134" y="350" width="38" height="46" rx="3" fill="none" stroke="var(--collab-blue)" stroke-width="6"/>
        <rect x="156" y="338" width="38" height="46" rx="3" fill="none" stroke="var(--collab-blue)" stroke-width="6"/>
      </g>

      <g class="icon-persevering">
        <circle cx="455" cy="95" r="62" fill="var(--ink-white)"/>
        <circle cx="468" cy="80" r="26" fill="var(--persevere-red)"/>
        <path d="M418 132 L500 100" stroke="var(--persevere-red)" stroke-width="4" fill="none"/>
      </g>

      <g class="icon-reflection">
        <circle cx="420" cy="450" r="62" fill="var(--ink-white)"/>
        <path d="M392 465 c-16 -4 -16 -26 0 -28 c0 -16 20 -22 30 -12 c10 -10 32 -4 30 12 c14 4 12 26 -4 28 c-2 10 -14 14 -22 8 v16 h-14 v-20 c-8 2 -18 2 -20 -4 z"
              fill="var(--reflect-yellow)"/>
      </g>

      <g class="icon-planning">
        <circle cx="202" cy="620" r="60" fill="var(--ink-white)"/>
        <rect x="174" y="593" width="40" height="54" rx="3" fill="none" stroke="var(--plan-orange)" stroke-width="5"/>
        <path d="M182 607 H206 M182 619 H206 M182 631 H198" stroke="var(--plan-orange)" stroke-width="4"/>
        <path d="M200 647 L234 601 L242 607 L208 653 L198 657 Z" fill="var(--plan-orange)"/>
      </g>

      <text class="habit-label" font-size="43" text-anchor="middle"
            transform="translate(75 268) rotate(-90)">COLLABORATION</text>
      <text class="habit-label" font-size="48" text-anchor="middle"
            transform="translate(434 256) rotate(-35.7)">PERSEVERING</text>
      <text class="habit-label" font-size="60" text-anchor="middle"
            transform="translate(560 606) rotate(-90)">REFLECTION</text>
      <text class="habit-label" font-size="58" x="28" y="758">PLANNING</text>
    </svg>
  </section>
</main>
</body>
</html>
```